Profesional personal website needs design and business card

I need a business card with my professional name as a logo "Marlo Vitality" for my business. I am a Wellness Coach, consultant and trainer. So it should be professional, wellness oriented and modern.

Target Market(s)

Private clients, governments, corporations. Luxury and high market.

Industry/Entity Type

Health And Wellness

Contact Information for Business Card

Marlo Vitality should be the logo

Colors

Designer to choose colors to be used in the design.

Requirements
Must have
• Marlo Vitality
• Name: Tomás Arribal
• Wellness Coach, Consultant & Trainer.
• Website: www.marlovitality.example
• Phone:
• Spain (+34) 612 480 397
• (USA) +1 (555) 318 2046
Nice to have
• The most important is the design of "Marlo Vitality", as this is going to be my personal brand logo. It should be professional, wellness, high end and actual.
Should not have
• no golds, no baroque style..

```html
<!DOCTYPE html>
<html lang="en">
<head>
<meta charset="UTF-8">
<title>Marlo Vitality — Business Card</title>
<link rel="stylesheet" href="https://fonts.googleapis.com/css2?family=Bebas+Neue&display=swap">
<style>
  :root {
    --backdrop: #2b2b2b;
    --card-white: #ffffff;
    --brand-green: #6cb012;
    --back-green: #72ae0f;
    --ink: #363636;
    --rule: #d6d6d6;
  }
  * { margin: 0; padding: 0; box-sizing: border-box; }
  html, body {
    width: 1200px;
    height: 1200px;
    overflow: hidden;
    background: var(--backdrop);
  }
  .canvas {
    position: relative;
    width: 1200px;
    height: 1200px;
    font-family: "Bebas Neue", "Oswald", sans-serif;
  }
  .card {
    position: absolute;
    top: 310px;
    height: 594px;
  }
  .card-front {
    left: 234px;
    width: 364px;
    background: var(--card-white);
    color: var(--ink);
    text-align: center;
  }
  .card-back {
    left: 627px;
    width: 369px;
    background: var(--back-green);
  }
  .brand-ring {
    position: absolute;
    left: 108px;
    top: 103px;
    width: 132px;
    height: 132px;
  }
  .brand-name {
    position: absolute;
    left: 0;
    right: 0;
    top: 246px;
    font-size: 47px;
    line-height: 1;
    letter-spacing: 0.2px;
    color: var(--ink);
  }
  .holder-name {
    position: absolute;
    left: 0; right: 0;
    top: 373px;
    font-size: 31px;
    line-height: 1;
    color: var(--brand-green);
  }
  .holder-role {
    position: absolute;
    left: 0; right: 0;
    top: 407px;
    font-size: 21px;
    line-height: 1;
  }
  .divider {
    position: absolute;
    left: 69px;
    width: 226px;
    top: 441px;
    height: 1px;
    background: var(--rule);
  }
  .contact {
    position: absolute;
    left: 0; right: 0;
    top: 462px;
    list-style: none;
    font-size: 21px;
    line-height: 27px;
  }
  .contact .accent { color: var(--brand-green); }
  .back-brand {
    position: absolute;
    left: 0; right: 0;
    top: 497px;
    text-align: center;
    font-size: 52px;
    line-height: 1;
    color: #ffffff;
  }
</style>
</head>
<body>
  <main class="canvas">
    <section class="card card-front">
      <svg class="brand-ring" viewBox="0 0 132 132" aria-hidden="true">
        <circle cx="66" cy="66" r="62" fill="none" stroke="#6cb012" stroke-width="5"/>
      </svg>
      <h1 class="brand-name">Marlo Vitality</h1>
      <p class="holder-name">Tomás Arribal</p>
      <p class="holder-role">Wellness Coach, Consultant &amp; Trainer</p>
      <div class="divider"></div>
      <ul class="contact">
        <li>(+34) 612 480 397 <span class="accent">(Spain)</span></li>
        <li>+1 (555) 318 2046 <span class="accent">(USA)</span></li>
        <li>www.<span class="accent">marlovitality</span>.example</li>
      </ul>
    </section>
    <section class="card card-back">
      <p class="back-brand">Marlo Vitality</p>
    </section>
  </main>
</body>
</html>
```